Website Design for Harbor 7340

We need a website design for a new company that strives to provide training and structure for religious missionaries who are traveling the world to teach of christianity.
They provide training in:
- Nutrition Coaching & Daily assignments
- Personal Training Sessions
- Phycological emotional/mental component
The goal of Harbor 7340 is to help missionaries preach the gospel of christ to those who haven't heard it due to geographical obstacles and physical limitations that get in the way.
The homepage template has linked images to use. If any other images are needed, stock images are acceptable.

Logo/Color Scheme: https://files.quorvex.net/share/8Kd2Lm9XpQ4rTz7WvN3bYc6HsJ1aFe0Gu

Customer Avatar/Core Message Canvas: https://sheets.plendora.net/s/4Rq81ZtyMn2wXcVb7KpLd0HsJ9aFgE3QuTo6YiPxNe/view

Homepage Template: https://docs.plendora.net/d/7Nw52KxpTr8vYzQm3LcBf1GhJ6dSeA0RuWo4XiZqPk/view

```html
<!DOCTYPE html>
<html lang="en">
<head>
<meta charset="utf-8">
<title>Harbor 7340 — Missionary Training</title>
<link href="https://fonts.googleapis.com/css2?family=Montserrat:ital,wght@0,400;0,500;0,600;0,700;1,600&display=swap" rel="stylesheet">
<style>
:root{
  --green:#3a4a1f;
  --green-deep:#2c3817;
  --yellow:#e9c148;
  --yellow-soft:#f3dc8c;
  --ink:#2a2a2a;
  --dark:#2c2c2c;
  --dark-2:#262626;
  --grey:#bdbdbd;
  --ring:#e6ead8;
  --white:#ffffff;
  --muted:#555;
}
*{box-sizing:border-box;margin:0;padding:0}
html,body{width:1200px;height:4211px;overflow:hidden}
body{font-family:'Montserrat',sans-serif;color:var(--ink);background:#fff}
.page{position:relative;width:1200px;height:4211px;overflow:hidden}
.abs{position:absolute}
.btn{position:absolute;display:flex;align-items:center;justify-content:center;border-radius:8px;font-weight:600;font-size:15px;color:var(--green-deep);background:var(--yellow)}
.btn-outline{background:transparent;border:2px solid var(--yellow);color:var(--yellow)}

/* nav */
.nav{top:0;left:0;width:1200px;height:84px;background:#fff}
.brand{font-weight:700;font-size:30px;color:var(--green);white-space:nowrap}
.nav-brand{left:52px;top:22px}
.nav-links{left:477px;top:31px;display:flex;gap:22px;font-size:15px;font-weight:500}
.nav-links .active{border-bottom:3px solid var(--yellow);padding-bottom:6px}
.nav-signup{left:1046px;top:24px;width:103px;height:34px;border-radius:9px;font-size:15px}

/* hero */
.hero{top:84px;left:0;width:1200px;height:648px;background:radial-gradient(ellipse at 60% 45%,#8a8a8a 0%,#4b4b4b 35%,#1c1c1c 75%,#0f0f0f 100%)}
.hero-title{left:50px;top:352px;font-size:30px;font-weight:600;color:#fff;line-height:41px}
.hero-sub{left:68px;top:446px;font-size:14.5px;font-weight:600;color:var(--yellow);line-height:21px}
.hero-btn1{left:68px;top:571px;width:230px;height:52px}
.hero-btn2{left:340px;top:571px;width:230px;height:52px;border-radius:8px}

/* staff */
.section-title{position:absolute;left:0;width:1200px;text-align:center;font-size:20px;font-weight:600;color:var(--green)}
.staff{position:absolute;width:150px;text-align:center}
.staff-ring{width:150px;height:150px;border-radius:50%;background:var(--ring);display:flex;align-items:center;justify-content:center}
.staff-ring.warm{background:#fbf3d8}
.staff-icon{width:124px;height:124px;border-radius:50%}
.staff-icon.green{background:var(--green);box-shadow:inset 0 0 0 8px #5a6b33}
.staff-icon.gold{background:var(--yellow);box-shadow:inset 0 0 0 8px var(--yellow-soft)}
.staff-label{font-size:15px;font-weight:600;margin-top:10px;line-height:20px}

/* dark sections */
.dark{left:0;width:1200px;background:var(--dark);color:#fff}
.dark-title{position:absolute;left:0;width:1200px;text-align:center;font-size:21px;font-weight:600}
.dark-text{position:absolute;left:0;width:1200px;text-align:center;font-size:14.5px;font-weight:600;line-height:20px}

/* approach */
.photo{position:absolute;border-radius:10px}
.dots{position:absolute;background:#e2e2e2}
.pillar{position:absolute;border-left:3px solid var(--yellow);padding-left:22px}
.pillar.right{border-left:none;border-right:3px solid var(--yellow);padding-left:0;padding-right:22px;text-align:right}
.pillar h3{font-size:20px;font-weight:600;color:var(--green);margin-bottom:28px}
.pillar p{font-size:14.5px;line-height:20px;color:var(--muted)}

/* form */
.form{top:3571px;left:0;width:1200px;height:347px;background:var(--grey)}
.form-title{position:absolute;left:0;top:40px;width:1200px;text-align:center;font-size:21px;font-weight:600;color:var(--green);line-height:26px}
.field-label{position:absolute;font-size:14px;color:var(--ink)}
.field{position:absolute;border:1px solid #8f8f8f;background:#c9c9c9;border-radius:3px;font-size:11px;color:#6d6d6d;padding:11px 12px}
.form-note{position:absolute;left:730px;top:128px;width:300px;text-align:center;font-size:14.5px;line-height:20px;color:var(--ink)}

/* footer */
.footer{top:3918px;left:0;width:1200px;height:293px;background:var(--dark-2);color:#fff}
.foot-links{position:absolute;left:270px;top:33px;width:650px;display:flex;justify-content:center;font-size:15px;font-weight:500;padding-bottom:10px;border-bottom:1px solid #555}
.foot-links span{padding:0 10px;border-right:1px solid #777}
.foot-links span:last-child{border-right:none}
.foot-info{position:absolute;font-size:11px;line-height:14px;font-weight:500}
.foot-copy{position:absolute;left:0;top:191px;width:1200px;text-align:center;font-size:11px}
.social{position:absolute;top:226px;width:34px;height:34px;border-radius:50%;background:var(--yellow)}
</style>
</head>
<body>
<div class="page">

  <!-- navigation -->
  <header class="abs nav">
    <div class="abs brand nav-brand">Harbor 7340</div>
    <nav class="abs nav-links">
      <span class="active">Home</span><span>Programs</span><span>Events</span><span>Online Store</span><span>About Us</span><span>Contact Us</span>
    </nav>
    <div class="btn nav-signup">Sign-up</div>
  </header>

  <!-- hero -->
  <section class="abs hero" role="img" aria-label="Black and white photograph of many hands reaching toward one another"></section>
  <h1 class="abs hero-title">“Empowering Change: By Illuminating<br>&nbsp;Lives Unexposed to The Gospel’s Light”</h1>
  <p class="abs hero-sub">Harbor 7340’s mission is to enable the word of Jesus to be experienced<br>by people in the most remote and treacherous parts of the world</p>
  <div class="btn btn-outline hero-btn1">View Our Programs</div>
  <div class="btn hero-btn2">Register for Training</div>

  <!-- staff -->
  <h2 class="section-title" style="top:786px">Harbor 7340’s Well-Rounded Staff for Specialized Training</h2>
  <div class="staff" style="left:95px;top:865px"><div class="staff-ring"><div class="staff-icon green" role="img" aria-label="Pastor icon"></div></div><div class="staff-label">Pastor</div></div>
  <div class="staff" style="left:233px;top:943px"><div class="staff-ring warm"><div class="staff-icon gold" role="img" aria-label="Nutritionist icon"></div></div><div class="staff-label">Nutritionist</div></div>
  <div class="staff" style="left:373px;top:865px"><div class="staff-ring"><div class="staff-icon green" role="img" aria-label="Former ranger icon"></div></div><div class="staff-label">Former<br>Ranger</div></div>
  <div class="staff" style="left:519px;top:943px"><div class="staff-ring warm"><div class="staff-icon gold" role="img" aria-label="Former special ops icon"></div></div><div class="staff-label">Former<br>Special Ops</div></div>
  <div class="staff" style="left:667px;top:865px"><div class="staff-ring"><div class="staff-icon green" role="img" aria-label="Dietician icon"></div></div><div class="staff-label">Dietician</div></div>
  <div class="staff" style="left:813px;top:943px"><div class="staff-ring warm"><div class="staff-icon gold" role="img" aria-label="Professional trainer icon"></div></div><div class="staff-label">Professional<br>Trainer</div></div>
  <div class="staff" style="left:961px;top:865px"><div class="staff-ring"><div class="staff-icon green" role="img" aria-label="Psychologist icon"></div></div><div class="staff-label">Psychologist</div></div>

  <!-- why -->
  <section class="abs dark" style="top:1215px;height:492px">
    <h2 class="dark-title" style="top:62px">Why Harbor 7340 is Breaking Barriers</h2>
    <p class="dark-text" style="top:132px">Geographical challenges make some communities difficult for missionaries to reach. The Harbor 7340 program is designed to remove the<br>physical limitations that can hinder us from bringing the Gospel to places that seem physically impossible to reach. Harbor 7340<br>is founded on Romans 15:20. In his letter to the Romans, Paul requests funding to take the Gospel to Spain. In this letter, he writes:</p>
    <p class="dark-text" style="top:224px;font-style:italic">”[20] and thus I make it my ambition to preach the gospel, not where Christ has already been<br>named, lest I build on someone else’s foundation, [21] but it is written, “those who<br>have never been told of him will see, and those who have never heard will understand.”</p>
    <p class="dark-text" style="top:305px;font-style:italic">(Romans 15:20-21)</p>
    <div class="btn" style="left:485px;top:390px;width:230px;height:52px">Join Our Mission</div>
  </section>

  <!-- approach -->
  <h2 class="section-title" style="top:1771px">Harbor 7340 Missionary Training Approach</h2>
  <p class="abs" style="left:0;top:1797px;width:1200px;text-align:center;font-size:15px;font-weight:600;color:var(--green)">Mind - Body - Spirit</p>

  <div class="dots" style="left:108px;top:1855px;width:125px;height:214px"></div>
  <div class="photo" style="left:153px;top:1901px;width:437px;height:291px;background:linear-gradient(90deg,#f1ede8 0%,#e7d7c4 40%,#b06a2e 60%,#2a2622 85%,#efe9e2 100%)" role="img" aria-label="Silhouette of a head filled with a sunset over the sea"></div>
  <div class="pillar" style="left:625px;top:1955px;width:520px;height:118px"><h3>Mind</h3><p>Psychologically, we will prepare the mind through counseling,<br>breathing techniques, and simulations in order to prepare for<br>psychological challenges that come with being in the field.</p></div>

  <div class="dots" style="left:967px;top:2148px;width:125px;height:214px"></div>
  <div class="photo" style="left:608px;top:2192px;width:438px;height:290px;background:radial-gradient(ellipse at 55% 60%,#b9734a 0%,#5a3524 35%,#1d1512 75%)" role="img" aria-label="Runner's feet on a road with glowing light and sparks"></div>
  <div class="pillar right" style="left:50px;top:2250px;width:508px;height:140px"><h3>Body</h3><p>Physically, we will prepare the body to overcome any physical<br>limitations through rigorous exercises and nutritional coaching<br>geared specifically to the geographical area the missionary<br>lans to go.</p></div>

  <div class="dots" style="left:108px;top:2435px;width:125px;height:214px"></div>
  <div class="photo" style="left:153px;top:2480px;width:437px;height:293px;background:linear-gradient(180deg,#d9c9a5 0%,#e6c278 40%,#8a6a3c 70%,#4a3a22 100%)" role="img" aria-label="Raised hands releasing birds into a golden sunset sky"></div>
  <div class="pillar" style="left:625px;top:2535px;width:520px;height:160px"><h3>Spirit</h3><p>Spiritually, we will prepare the soul to overcome spiritual<br>challenges that arise in different areas of the world. Our<br>curriculum is designed to prepare missionaries with a firm base<br>of theological principles and destination specific training for the<br>area in which the missionary is going.</p></div>

  <div class="btn" style="left:440px;top:2836px;width:320px;height:52px">View our detailed training program</div>

  <!-- who -->
  <section class="abs dark" style="top:2940px;height:631px;background:linear-gradient(135deg,#2f2f2f,#242424)" role="img" aria-label="Dim background photograph of an open bible and map">
    <h2 class="dark-title" style="top:61px">Who is Harbor 7340 For?</h2>
    <p class="dark-text" style="top:140px;font-size:14.5px">Sending Agencies for Missionaries</p>
    <p class="dark-text" style="top:180px;font-weight:500">Are you looking to improve the training you’re offering your flock? We have designed a program to align our training with<br>your goals to spread the Gospel to people and places where Jesus remains unnamed &amp; unknown. Our training helps turn<br>your missionaries to resilient, well-trained men and women.</p>
    <p class="dark-text" style="top:262px">Missionaries</p>
    <p class="dark-text" style="top:302px;font-weight:500">Are you independently seeking to develop your knowledge and skills independently? We are here to help!<br>We can customize a training approach that fits your specific needs. Let us support your missionary journey<br>to spread the Gospel to the most remote and treacherous areas in the world.</p>
    <p class="dark-text" style="top:384px">Christian-based training program for ALL!</p>
    <p class="dark-text" style="top:424px;font-weight:500">Are you looking to support the missionary community? Well we have a solution for you! We also offer a customized, personal-<br>training approach for everyone. Even if you’re not preparing for a mission, joining one of our training programs will<br>allow you to support our missionaries through your own physical fitness journey.</p>
    <div class="btn" style="left:440px;top:530px;width:320px;height:52px">View our Training Options</div>
  </section>

  <!-- newsletter form -->
  <section class="abs form">
    <h2 class="form-title">Join our Missionary Training: Stay up-to-date on our training programs,<br>missionary success stories, and new program info!</h2>
    <span class="field-label" style="left:168px;top:116px">Your Name</span>
    <div class="field" style="left:168px;top:135px;width:228px;height:37px">Mara Vell</div>
    <span class="field-label" style="left:171px;top:186px">Your Phone Nuber</span>
    <div class="field" style="left:168px;top:205px;width:228px;height:37px">(+125 123-4567-89)</div>
    <span class="field-label" style="left:168px;top:256px">Email Address</span>
    <div class="field" style="left:168px;top:275px;width:228px;height:37px">maravell@example.com</div>
    <span class="field-label" style="left:418px;top:116px">Your Message:</span>
    <div class="field" style="left:418px;top:135px;width:300px;height:177px"></div>
    <p class="form-note">Subscribe and help us in supporting<br>our &nbsp;missionaries as they spread the<br>Gospel to all corners and areas<br>of the world</p>
    <div class="btn" style="left:768px;top:252px;width:230px;height:50px">Submit Now</div>
  </section>

  <!-- footer -->
  <footer class="abs footer">
    <div class="foot-links"><span>Home</span><span>Programs</span><span>Events</span><span>Online Store</span><span>About Us</span><span>Contact Us</span><span>Sign-up</span></div>
    <svg class="abs" style="left:272px;top:104px" width="36" height="36" viewBox="0 0 36 36" aria-hidden="true"><circle cx="18" cy="18" r="18" fill="#e9c148"/><path d="M18 8a7 7 0 0 0-7 7c0 5 7 13 7 13s7-8 7-13a7 7 0 0 0-7-7z" fill="#262626"/><circle cx="18" cy="15" r="2.6" fill="#e9c148"/></svg>
    <p class="foot-info" style="left:331px;top:104px"><b>Office Location:</b><br>218 Larkspur Rd<br>Fenmoor, NJ 08417</p>
    <div class="abs brand" style="left:520px;top:104px;color:#fff;font-size:26px">Harbor 7340</div>
    <svg class="abs" style="left:760px;top:104px" width="36" height="36" viewBox="0 0 36 36" aria-hidden="true"><circle cx="18" cy="18" r="18" fill="#e9c148"/><path d="M12 9l4 0 2 5-2.5 2a12 12 0 0 0 5.5 5.5l2-2.5 5 2v4a2 2 0 0 1-2 2A18 18 0 0 1 10 11a2 2 0 0 1 2-2z" fill="#262626"/></svg>
    <p class="foot-info" style="left:820px;top:112px"><b>Call Us:</b><br>415-207-6618</p>
    <p class="foot-copy">Copyright © 2023 Harbor 7340 &nbsp;|&nbsp; Terms Of Service &nbsp;|&nbsp; Privacy Policy.</p>
    <div class="social" style="left:538px" role="img" aria-label="Social link"></div>
    <div class="social" style="left:583px" role="img" aria-label="Social link"></div>
    <div class="social" style="left:628px" role="img" aria-label="Social link"></div>
  </footer>

</div>
</body>
</html>
```